In Dash GPS

My Business is a small family owned and operated company.
Our specialty is In dash GPS systems.
These systems are All touch screen with built in bluetooth, AM/FM RDS radio, GPS, USB, Zunetta integration, DVD/MP3/CD/SD, steering wheel controls still work.
Product is installed by a experienced installer, and is local.
ALL MAKES AND MODELS AVAILABLE!
I do a lot of work for car dealerships and private buyers..
These are some of my competitors websites:
http://www.plovernav.com.au/index.php
http://www.quenlo.com.au/Integrated-GPS-Systems-s/582.htm
http://www.dash-tember.co.uk/226-marlow-navi-dvd
Im looking for a flyer I can put up in car dealerships to advertise the different work I can offer.
I have attached a copy of my business card and logo for your convenience.
The colours on the business card are the main ones I want to use.
I have also uploaded some of the work I have done
Target Market(s)
NEW and USED car buyers, private buyers

```html
<!DOCTYPE html>
<html lang="en">
<head>
<meta charset="utf-8">
<title>Push the Button and Drive – Larkin Installs</title>
<link rel="stylesheet" href="https://fonts.googleapis.com/css2?family=Alfa+Slab+One&family=Open+Sans:wght@300;400;600&display=swap">
<style>
  :root {
    --bg-top: #1d2b3f;
    --bg-bottom: #0b0e15;
    --footer-bg: #121212;
    --glow: #1fa8ff;
    --glow-soft: rgba(31, 168, 255, 0.55);
    --headline-fill: #0c1622;
    --screen-centre: #8a8588;
    --screen-edge: #3a3438;
    --white: #ffffff;
  }
  * { margin: 0; padding: 0; box-sizing: border-box; }
  html, body { width: 1200px; height: 846px; overflow: hidden; background: var(--bg-bottom); }
  .flyer {
    position: relative;
    width: 1200px;
    height: 846px;
    overflow: hidden;
    background: linear-gradient(180deg, var(--bg-top) 0%, #151f2e 45%, var(--bg-bottom) 100%);
    font-family: "Open Sans", Arial, sans-serif;
    color: var(--white);
  }
  .power-icon { position: absolute; left: 52px; top: 46px; width: 124px; height: 124px; }
  .headline {
    position: absolute;
    left: 204px;
    top: 58px;
    font-family: "Alfa Slab One", Georgia, serif;
    font-weight: 400;
    color: var(--headline-fill);
    text-shadow: 0 0 2px var(--glow), 0 0 6px var(--glow), 0 0 12px var(--glow-soft);
    line-height: 1;
  }
  .headline-top { display: block; font-size: 34px; letter-spacing: 1px; }
  .headline-bottom { display: block; font-size: 60px; margin-top: 2px; }
  .brand-name {
    position: absolute;
    right: 74px;
    top: 58px;
    width: 330px;
    text-align: right;
    font-family: "Open Sans", Arial, sans-serif;
    font-weight: 600;
    font-size: 44px;
    line-height: 1.05;
    color: var(--white);
  }
  .screen-grid {
    position: absolute;
    left: 62px;
    top: 194px;
    display: grid;
    grid-template-columns: repeat(3, 311px);
    grid-template-rows: repeat(2, 158px);
    column-gap: 71px;
    row-gap: 26px;
  }
  .sample-screen {
    display: flex;
    align-items: center;
    justify-content: center;
    border: 2px solid var(--glow);
    border-radius: 17px;
    background: radial-gradient(ellipse at 50% 45%, var(--screen-centre) 0%, #6b6569 45%, var(--screen-edge) 100%);
    box-shadow: 0 0 10px var(--glow-soft), 0 0 3px var(--glow);
    font-family: "Alfa Slab One", Georgia, serif;
    font-size: 29px;
    color: var(--white);
    letter-spacing: 0.5px;
  }
  .tagline {
    position: absolute;
    left: 0;
    width: 1200px;
    top: 588px;
    text-align: center;
    font-family: "Alfa Slab One", Georgia, serif;
    font-size: 46px;
    letter-spacing: 1px;
    color: var(--white);
  }
  .divider { position: absolute; left: 0; top: 673px; width: 1200px; height: 6px; background: var(--white); }
  .contact-band {
    position: absolute;
    left: 0;
    top: 679px;
    width: 1200px;
    height: 167px;
    background: linear-gradient(180deg, #1a1a1a 0%, var(--footer-bg) 100%);
    text-align: center;
    font-weight: 300;
  }
  .contact-role { margin-top: 21px; font-size: 31px; line-height: 44px; }
  .contact-details { margin-top: 12px; font-size: 29px; line-height: 42px; }
</style>
</head>
<body>
<main class="flyer">
  <svg class="power-icon" viewBox="0 0 120 120" aria-hidden="true">
    <defs>
      <filter id="icon-glow" x="-30%" y="-30%" width="160%" height="160%">
        <feGaussianBlur stdDeviation="3" result="blur"/>
        <feMerge><feMergeNode in="blur"/><feMergeNode in="SourceGraphic"/></feMerge>
      </filter>
    </defs>
    <g filter="url(#icon-glow)" fill="none" stroke="#1fa8ff">
      <circle cx="60" cy="60" r="52" stroke-width="3"/>
      <circle cx="60" cy="60" r="46" stroke="#0c1622" stroke-width="8"/>
      <path d="M44 42 A24 24 0 1 0 76 42" stroke-width="9" stroke-linecap="round"/>
      <line x1="60" y1="30" x2="60" y2="60" stroke-width="9" stroke-linecap="round"/>
    </g>
  </svg>

  <h1 class="headline">
    <span class="headline-top">PUSH THE BUTTON</span>
    <span class="headline-bottom">and DRIVE!</span>
  </h1>

  <p class="brand-name">Larkin<br>Installs</p>

  <section class="screen-grid">
    <div class="sample-screen">SAMPLE SCREEN</div>
    <div class="sample-screen">SAMPLE SCREEN</div>
    <div class="sample-screen">SAMPLE SCREEN</div>
    <div class="sample-screen">SAMPLE SCREEN</div>
    <div class="sample-screen">SAMPLE SCREEN</div>
    <div class="sample-screen">SAMPLE SCREEN</div>
  </section>

  <p class="tagline">ALL MAKES AND MODELS AVAILABLE!</p>

  <div class="divider"></div>

  <footer class="contact-band">
    <p class="contact-role">Installation Technician</p>
    <p class="contact-details">Sam Larkin | 0400 555 218 | samlarkin@larkinmail.com</p>
  </footer>
</main>
</body>
</html>
```